Customizing and design a blog from the scratch

I need a blog designer to customize my blog from scratch, I have create the blog with Wordpress with Divi theme but I have nothing to do with the layout and the design, I can only provide the menu list I have in my mind and the skill of writing,I need a talented blog designer to help me with that.Thanks

Colors

Designer to choose colors to be used in the design.

Requirements
Nice to have
• My blog name is
• Follow the quiet river
• So I would like an inspiring background, the blog will be having 5 main pages
• 1. Education
• 2.Kids corner
• 3.Health and fitness
• 4.Beauty and fashion
• 5.Arabian corner
• UNDER each of them I will post a daily new post.
• I would like to have a home page which side will write a brief post a bout the page.
• Hope that helps!

```html
<!DOCTYPE html>
<html lang="en">
<head>
<meta charset="utf-8">
<title>Follow the quiet river</title>
<link href="https://fonts.googleapis.com/css2?family=Quicksand:wght@500;600;700&family=Lato:wght@400;700&display=swap" rel="stylesheet">
<style>
:root{
  --orange:#fb6a10;
  --black:#111111;
  --ink:#2b2b2b;
  --muted:#777777;
  --line:#fb6a10;
  --sky:#3b9bd8;
  --navy:#35529a;
  --white:#ffffff;
}
*{box-sizing:border-box;margin:0;padding:0}
html,body{width:1200px;height:3940px;overflow:hidden}
body{position:relative;background:var(--white);font-family:'Lato',sans-serif;color:var(--ink)}
.abs{position:absolute}
.ph{display:block}
/* header */
.topbar{left:0;top:0;width:1200px;height:107px;background:var(--black)}
.brand{font-family:'Quicksand',sans-serif;font-weight:600;color:var(--white);font-size:29px;left:110px;top:34px}
.search{left:812px;top:33px;width:276px;height:41px;border:1px solid #555;display:flex;align-items:center}
.search span{flex:1;color:#ccc;font-size:13px;padding-left:12px}
.search b{width:41px;height:41px;background:var(--orange);display:flex;align-items:center;justify-content:center}
.nav{left:0;top:107px;width:1200px;height:61px;background:var(--orange)}
.nav ul{list-style:none;display:flex;position:absolute;left:110px;top:0;height:61px}
.nav li{color:var(--white);font-family:'Quicksand',sans-serif;font-weight:600;font-size:15px;display:flex;align-items:center;padding:0 21px}
.nav li.active{background:var(--black);padding:0 36px}
/* hero */
.hero{left:112px;top:206px;width:976px;height:548px;background:linear-gradient(100deg,#3a3330 0%,#5b4a40 40%,#7b6555 60%,#2e2a28 100%)}
.hero h1{position:absolute;left:36px;top:210px;font-family:'Quicksand',sans-serif;font-weight:700;font-size:45px;color:var(--white)}
.hero h1 em{font-style:normal;color:var(--orange)}
.hero p{position:absolute;left:39px;top:283px;width:470px;color:#eee;font-size:15px;line-height:30px}
.btn{position:absolute;left:39px;top:392px;background:var(--orange);color:var(--white);font-family:'Quicksand',sans-serif;font-weight:700;font-size:17px;padding:12px 14px;border-radius:2px}
/* section heads */
.shead{height:41px;border-bottom:2px solid var(--line)}
.shead .tab{display:inline-block;height:39px;background:var(--orange);color:var(--white);font-family:'Quicksand',sans-serif;font-weight:600;font-size:20px;line-height:39px;padding:0 40px 0 18px;clip-path:polygon(0 0,calc(100% - 14px) 0,100% 100%,0 100%)}
.arrows{position:absolute;right:0;top:8px;display:flex;gap:5px}
.arrows i{width:24px;height:24px;border:1px solid #aaa;border-radius:50%;display:flex;align-items:center;justify-content:center}
/* cards */
.card3{width:219px}
.card3 .ph{width:219px;height:165px}
.card3 h3{font-weight:400;font-size:16px;margin-top:17px;color:#333}
.meta{display:flex;gap:10px;font-size:11px;color:#777;margin-top:14px;align-items:center;white-space:nowrap}
.meta span{display:flex;align-items:center;gap:4px}
.ico{width:10px;height:10px;fill:none;stroke:#888;stroke-width:1.4;flex:none}
.big{width:324px}
.big .ph{width:324px;height:205px}
.big h3{font-family:'Quicksand',sans-serif;font-weight:600;font-size:14.5px;line-height:24px;margin-top:19px;color:#333;width:324px}
.byline{display:flex;align-items:center;font-size:12px;color:#555;margin-top:12px;gap:8px;width:316px;white-space:nowrap}
.byline .c{margin-left:auto;width:16px;height:14px;border:1.5px solid #4a4;border-radius:2px;font-size:8px;color:#4a4;display:flex;align-items:center;justify-content:center;flex:none}
.small{display:flex;gap:21px;width:320px}
.small .ph{flex:none}
.small h4{font-family:'Quicksand',sans-serif;font-weight:600;font-size:13px;line-height:21px;color:#333;white-space:nowrap}
.small .meta{margin-top:8px}
/* featured */
.feat{display:flex;gap:10px}
.feat p{width:182px;font-size:12.5px;line-height:22px;color:#444}
.feat small{display:block;margin-top:8px;font-size:10px;color:var(--orange);font-style:italic;text-decoration:underline}
.feat .ph{width:85px;height:84px;flex:none;position:relative}
.feat .cnt{position:absolute;right:2px;top:3px;width:22px;height:13px;background:#222;color:#fff;font-size:8px;text-align:center;line-height:13px}
/* social widget */
.wtabs{left:812px;top:1241px;display:flex;gap:3px}
.wtabs div{height:31px;color:var(--white);font-family:'Quicksand',sans-serif;font-weight:700;font-size:15px;display:flex;align-items:center;justify-content:center}
.wtabs .t1{width:110px;background:var(--sky)}
.wtabs .t2{width:110px;background:var(--navy)}
.wbox{left:812px;top:1272px;width:276px;height:358px;border:7px solid var(--sky);background:var(--white);padding:10px 8px;font-size:11.5px;color:#555;overflow:hidden}
.wbox .hd{color:var(--orange);font-size:12.5px;padding-bottom:10px;border-bottom:1px solid #ddd}
.tw{padding:14px 10px;border-bottom:1px solid #ddd;line-height:18px;width:240px}
.tw .row{display:flex;gap:10px;margin:10px 0}
.tw .av{width:40px;height:36px;border:1px solid #ccc;border-radius:3px;flex:none}
.scroll{position:absolute;right:4px;top:10px;width:6px;height:330px;background:#eee}
.scroll i{position:absolute;left:0;top:60px;width:6px;height:100px;background:#bbb}
/* newsletter */
.news{left:0;top:3474px;width:1200px;height:144px;background:var(--orange)}
.news .su{position:absolute;left:234px;top:42px;color:#fff;font-family:'Quicksand',sans-serif;font-weight:600;font-size:22px}
.news .nl{position:absolute;left:234px;top:72px;color:#fff;font-family:'Quicksand',sans-serif;font-weight:600;font-size:37px}
.field{position:absolute;left:469px;top:46px;width:591px;height:55px;background:#fff;border-radius:28px;display:flex;align-items:center;padding-left:24px;font-size:12px;color:#555;gap:8px}
.send{position:absolute;right:2px;top:2px;width:51px;height:51px;border-radius:50%;background:var(--orange);border:3px solid #fff;display:flex;align-items:center;justify-content:center}
/* footer */
.foot{left:0;top:3618px;width:1200px;height:322px;background:#1b1b1b;text-align:center;color:#fff}
.foot .brand2{position:absolute;left:0;width:1200px;top:58px;font-family:'Quicksand',sans-serif;font-weight:600;font-size:33px}
.fnav{position:absolute;left:0;width:1200px;top:127px;display:flex;justify-content:center;gap:22px;font-family:'Quicksand',sans-serif;font-weight:600;font-size:14px}
.fnav .s{color:#aaa}
.soc{position:absolute;left:0;width:1200px;top:178px;display:flex;justify-content:center;gap:7px}
.soc i{width:36px;height:36px;border:2px solid #fff;border-radius:50%;display:flex;align-items:center;justify-content:center}
.soc i b{width:10px;height:10px;background:#fff;border-radius:50%}
.copy{position:absolute;left:0;width:1200px;top:240px;font-size:13px;color:#ddd}
</style>
</head>
<body>
<svg width="0" height="0" style="position:absolute">
  <symbol id="cal" viewBox="0 0 10 10"><rect x="1" y="2" width="8" height="7"/><path d="M1 4.5h8M3 1v2M7 1v2"/></symbol>
  <symbol id="cmt" viewBox="0 0 10 10"><path d="M1 2h8v5H4l-2 2V7H1z"/></symbol>
  <symbol id="hrt" viewBox="0 0 10 10"><path d="M5 9 1.5 5.3A2 2 0 0 1 5 2.5a2 2 0 0 1 3.5 2.8z"/></symbol>
  <symbol id="clk" viewBox="0 0 10 10"><circle cx="5" cy="5" r="4"/><path d="M5 2.5V5h2"/></symbol>
</svg>

<header class="abs topbar">
  <div class="abs brand">Follow the quiet river</div>
  <div class="abs search"><span>Search</span><b><svg width="13" height="13" viewBox="0 0 14 14" fill="none" stroke="#fff" stroke-width="2"><circle cx="6" cy="6" r="4.3"/><path d="m9 9 4 4"/></svg></b></div>
</header>
<nav class="abs nav"><ul>
  <li class="active">Home</li><li>Education</li><li>Kids Corner</li><li>Health &amp; Fitness</li><li>Beauty &amp; Fashion</li><li>Arabian Corner</li><li>Contact Us</li>
</ul></nav>

<section class="abs hero" role="img" aria-label="Photo of a woman running on a treadmill in a gym">
  <h1>Follow the quiet <em>river</em></h1>
  <p>Sed ut perspiciatis unde omnis iste natus error sit voluptatem accusantium doloremque laudantium, totam rem aperiam, ea ipsa quae ab illo inventore veritatis</p>
  <span class="btn">Read More</span>
</section>

<!-- Education -->
<div class="abs shead" style="left:112px;top:804px;width:683px"><span class="tab">Education</span>
  <div class="arrows"><i><svg width="8" height="8" viewBox="0 0 8 8" fill="none" stroke="#666" stroke-width="1.3"><path d="M5 1 2 4l3 3"/></svg></i><i><svg width="8" height="8" viewBox="0 0 8 8" fill="none" stroke="#666" stroke-width="1.3"><path d="m3 1 3 3-3 3"/></svg></i></div></div>
<div class="abs card3" style="left:112px;top:872px"><div class="ph" role="img" aria-label="Open book in a library" style="background:linear-gradient(#7a4a32,#c9a27a)"></div><h3>Sed ut perspiciatis</h3>
  <div class="meta"><span><svg class="ico"><use href="#cal"/></svg>Sep 23, 2019</span><span><svg class="ico"><use href="#cmt"/></svg>4 Comments</span><span><svg class="ico"><use href="#hrt"/></svg>13</span></div></div>
<div class="abs card3" style="left:345px;top:872px"><div class="ph" role="img" aria-label="Classroom with students" style="background:linear-gradient(#c8ccd0,#4a4f5a)"></div><h3>Sed ut perspiciatis</h3>
  <div class="meta"><span><svg class="ico"><use href="#cal"/></svg>Sep 23, 2019</span><span><svg class="ico"><use href="#cmt"/></svg>4 Comments</span><span><svg class="ico"><use href="#hrt"/></svg>13</span></div></div>
<div class="abs card3" style="left:576px;top:872px"><div class="ph" role="img" aria-label="Child writing in a notebook" style="background:linear-gradient(#2f5a8a,#d9c5a8)"></div><h3>Sed ut perspiciatis</h3>
  <div class="meta"><span><svg class="ico"><use href="#cal"/></svg>Sep 23, 2019</span><span><svg class="ico"><use href="#cmt"/></svg>4 Comments</span><span><svg class="ico"><use href="#hrt"/></svg>13</span></div></div>

<!-- Featured -->
<div class="abs shead" style="left:812px;top:804px;width:276px"><span class="tab">Featured Post</span></div>
<div class="abs feat" style="left:812px;top:866px"><p>Sed ut perspiciatis unde omnis accusantium dolorem<small>20 Sep 2019 &nbsp;| &nbsp;Comments (05)</small></p><div class="ph" role="img" aria-label="Child reading a book" style="background:linear-gradient(#d8c0a0,#b04a2a)"><span class="cnt">2</span></div></div>
<div class="abs feat" style="left:812px;top:978px"><p>Sed ut perspiciatis unde omnis accusantium dolorem<small>20 Sep 2019 &nbsp;| &nbsp;Comments (05)</small></p><div class="ph" role="img" aria-label="Boy building a robot" style="background:linear-gradient(#9aa4ad,#3a4a5a)"><span class="cnt">2</span></div></div>
<div class="abs feat" style="left:812px;top:1091px"><p>Sed ut perspiciatis unde omnis accusantium dolorem<small>20 Sep 2019 &nbsp;| &nbsp;Comments (05)</small></p><div class="ph" role="img" aria-label="Laptop on a desk" style="background:linear-gradient(#5a6068,#c7c9cc)"><span class="cnt">2</span></div></div>

<!-- Social widget -->
<div class="abs wtabs"><div class="t1">Murmur</div><div class="t2">Circle</div></div>
<div class="abs wbox">
  <div class="hd">Murmur by @Follow the quiet river</div>
  <div class="tw">Follow the quiet river@loremipsum<div class="row"><span class="av"></span><span>Lorem Ipsum Dummy Text<br>@ Follow the quiet river</span></div>Sed ut perspiciatis unde omnis iste volu tatem santium doloremque.....</div>
  <div class="tw" style="border:0">Follow the quiet river@loremipsum<div class="row"><span class="av"></span><span>Lorem Ipsum Dummy Text<br>@ Follow the quiet river</span></div>Sed ut perspiciatis unde omnis iste volu tatem santium doloremque.....</div>
  <div class="scroll"><i></i></div>
</div>

<!-- Kids Corner -->
<div class="abs shead" style="left:112px;top:1166px;width:683px"><span class="tab">Kids Corner</span></div>
<div class="abs big" style="left:112px;top:1235px"><div class="ph" role="img" aria-label="Small boy holding a teddy bear" style="background:linear-gradient(#9aa7b4,#4b5868)"></div><h3>Contrary to popular belief, Lorem Ipsum is of classical Latin literature</h3>
  <div class="byline">Mara Linden &nbsp;- <svg class="ico"><use href="#cal"/></svg>September 28, 2019<span class="c">0</span></div></div>
<div class="abs big" style="left:471px;top:1235px"><div class="ph" role="img" aria-label="Child playing in a cardboard box" style="background:linear-gradient(#e8e2d8,#c89a6a)"></div><h3>Contrary to popular belief, Lorem Ipsum is of classical Latin literature</h3>
  <div class="byline">Mara Linden &nbsp;- <svg class="ico"><use href="#cal"/></svg>September 28, 2019<span class="c">0</span></div></div>
<div class="abs small" style="left:112px;top:1589px"><div class="ph" role="img" aria-label="Child with aviator goggles" style="width:104px;height:90px;background:linear-gradient(#8a9aa2,#6a5a48)"></div><div><h4>Contrary to popular belief,is not<br>simply random text.</h4><div class="meta"><span><svg class="ico"><use href="#clk"/></svg>September 28, 2019</span></div></div></div>
<div class="abs small" style="left:474px;top:1589px"><div class="ph" role="img" aria-label="Children running on grass" style="width:104px;height:90px;background:linear-gradient(#5a8ad0,#4a8a3a)"></div><div><h4>Contrary to popular belief,is not<br>simply random text.</h4><div class="meta"><span><svg class="ico"><use href="#clk"/></svg>September 28, 2019</span></div></div></div>
<div class="abs small" style="left:112px;top:1712px"><div class="ph" role="img" aria-label="Child with backpack on school steps" style="width:104px;height:90px;background:linear-gradient(#c89a80,#9a4a3a)"></div><div><h4>Contrary to popular belief,is not<br>simply random text.</h4><div class="meta"><span><svg class="ico"><use href="#clk"/></svg>September 28, 2019</span></div></div></div>
<div class="abs small" style="left:474px;top:1712px"><div class="ph" role="img" aria-label="Group of smiling children" style="width:104px;height:90px;background:linear-gradient(#6a8a5a,#a0503a)"></div><div><h4>Contrary to popular belief,is not<br>simply random text.</h4><div class="meta"><span><svg class="ico"><use href="#clk"/></svg>September 28, 2019</span></div></div></div>

<!-- Health and Fitness -->
<div class="abs shead" style="left:112px;top:1892px;width:683px"><span class="tab">Health and Fitness</span></div>
<div class="abs big" style="left:112px;top:1957px"><div class="ph" role="img" aria-label="People exercising in a gym" style="background:linear-gradient(#b8b0aa,#4a4040)"></div><h3>Contrary to popular belief, Lorem Ipsum is of classical Latin literature</h3>
  <div class="byline">Mara Linden &nbsp;- <svg class="ico"><use href="#cal"/></svg>September 28, 2019<span class="c">0</span></div></div>
<div class="abs small" style="left:477px;top:1957px"><div class="ph" role="img" aria-label="Woman drinking water outdoors" style="width:96px;height:84px;background:linear-gradient(#5a7a3a,#c86a6a)"></div><div><h4>Contrary to popular belief,is not<br>simply random text.</h4><div class="meta"><span><svg class="ico"><use href="#cal"/></svg>May 23, 2019</span><span><svg class="ico"><use href="#cmt"/></svg>4 Comments</span></div></div></div>
<div class="abs small" style="left:477px;top:2070px"><div class="ph" role="img" aria-label="Woman stretching on a mat" style="width:96px;height:84px;background:linear-gradient(#e4e0dc,#3a2a2a)"></div><div><h4>Contrary to popular belief,is not<br>simply random text.</h4><div class="meta"><span><svg class="ico"><use href="#cal"/></svg>May 23, 2019</span><span><svg class="ico"><use href="#cmt"/></svg>4 Comments</span></div></div></div>
<div class="abs small" style="left:477px;top:2182px"><div class="ph" role="img" aria-label="Woman running at sunset" style="width:96px;height:84px;background:linear-gradient(#5a8ab0,#8a5a3a)"></div><div><h4>Contrary to popular belief,is not<br>simply random text.</h4><div class="meta"><span><svg class="ico"><use href="#cal"/></svg>May 23, 2019</span><span><svg class="ico"><use href="#cmt"/></svg>4 Comments</span></div></div></div>

<!-- Beauty and Fashion -->
<div class="abs shead" style="left:112px;top:2320px;width:683px"><span class="tab">Beauty and Fashion</span></div>
<div class="abs big" style="left:112px;top:2387px"><div class="ph" role="img" aria-label="Woman with long wavy hair" style="background:linear-gradient(#6a4a38,#c89a7a)"></div><h3>Contrary to popular belief, Lorem Ipsum is of classical Latin literature</h3>
  <div class="byline">Mara Linden &nbsp;- <svg class="ico"><use href="#cal"/></svg>September 28, 2019<span class="c">0</span></div></div>
<div class="abs big" style="left:473px;top:2387px"><div class="ph" role="img" aria-label="Woman walking on a city street" style="background:linear-gradient(#a0908a,#5a5050)"></div><h3>Contrary to popular belief, Lorem Ipsum is of classical Latin literature</h3>
  <div class="byline">Mara Linden &nbsp;- <svg class="ico"><use href="#cal"/></svg>September 28, 2019<span class="c">0</span></div></div>
<div class="abs big" style="left:112px;top:2731px"><div class="ph" role="img" aria-label="Colourful beauty portrait" style="background:linear-gradient(110deg,#3a7ae0,#e04aa0,#28c0e8)"></div><h3>Contrary to popular belief, Lorem Ipsum is of classical Latin literature</h3>
  <div class="byline">Mara Linden &nbsp;- <svg class="ico"><use href="#cal"/></svg>September 28, 2019<span class="c">0</span></div></div>
<div class="abs big" style="left:473px;top:2731px"><div class="ph" role="img" aria-label="Hat and accessories on a mannequin" style="background:linear-gradient(#2a2018,#c8a070)"></div><h3>Contrary to popular belief, Lorem Ipsum is of classical Latin literature</h3>
  <div class="byline">Mara Linden &nbsp;- <svg class="ico"><use href="#cal"/></svg>September 28, 2019<span class="c">0</span></div></div>

<!-- Arabian Corner -->
<div class="abs shead" style="left:112px;top:3094px;width:683px"><span class="tab">Arabian Corner</span>
  <div class="arrows"><i><svg width="8" height="8" viewBox="0 0 8 8" fill="none" stroke="#666" stroke-width="1.3"><path d="M5 1 2 4l3 3"/></svg></i><i><svg width="8" height="8" viewBox="0 0 8 8" fill="none" stroke="#666" stroke-width="1.3"><path d="m3 1 3 3-3 3"/></svg></i></div></div>
<div class="abs card3" style="left:112px;top:3160px"><div class="ph" role="img" aria-label="Oil lamp with glowing smoke at night" style="background:linear-gradient(#1a2a4a,#8a6a3a)"></div><h3>Sed ut perspiciatis</h3>
  <div class="meta"><span><svg class="ico"><use href="#cal"/></svg>Sep 23, 2019</span><span><svg class="ico"><use href="#cmt"/></svg>4 Comments</span><span><svg class="ico"><use href="#hrt"/></svg>13</span></div></div>
<div class="abs card3" style="left:345px;top:3160px"><div class="ph" role="img" aria-label="Lantern glowing in the dark" style="background:linear-gradient(#161616,#3a2a1a)"></div><h3>Sed ut perspiciatis</h3>
  <div class="meta"><span><svg class="ico"><use href="#cal"/></svg>Sep 23, 2019</span><span><svg class="ico"><use href="#cmt"/></svg>4 Comments</span><span><svg class="ico"><use href="#hrt"/></svg>13</span></div></div>
<div class="abs card3" style="left:576px;top:3160px"><div class="ph" role="img" aria-label="Ornate lantern with warm light" style="background:linear-gradient(#5a3010,#e0a040)"></div><h3>Sed ut perspiciatis</h3>
  <div class="meta"><span><svg class="ico"><use href="#cal"/></svg>Sep 23, 2019</span><span><svg class="ico"><use href="#cmt"/></svg>4 Comments</span><span><svg class="ico"><use href="#hrt"/></svg>13</span></div></div>

<!-- Newsletter -->
<section class="abs news">
  <svg style="position:absolute;left:143px;top:34px" width="70" height="70" viewBox="0 0 70 70" fill="none" stroke="#fff" stroke-width="3" stroke-linejoin="round"><path d="M4 30v36h62V30L35 8z"/><path d="M14 38V16h42v22"/><path d="M22 24h26M22 31h26M22 38h18"/><path d="m4 30 31 22 31-22M4 66l24-19M66 66 42 47"/></svg>
  <div class="su">Sign Up</div>
  <div class="nl">Newsletter</div>
  <div class="field"><svg width="12" height="10" viewBox="0 0 12 10"><rect width="12" height="10" fill="#444"/><path d="m0 0 6 5 6-5" stroke="#fff" fill="none"/></svg>Enter Your Email...
    <span class="send"><svg width="18" height="18" viewBox="0 0 18 18" fill="#fff"><path d="M17 1 1 8l6 2 1 6 3-4 4 3z"/></svg></span></div>
</section>

<!-- Footer -->
<footer class="abs foot">
  <div class="brand2">Follow the quiet river</div>
  <div class="fnav"><span>Home</span><span class="s">/</span><span>Education</span><span class="s">/</span><span>Kids Corner</span><span class="s">/</span><span>Health &amp; Fitness</span><span class="s">/</span><span>Beauty &amp; Fashion</span><span class="s">/</span><span>Arabian Corner</span><span class="s">/</span><span>Contact Us</span></div>
  <div class="soc"><i><b></b></i><i><b></b></i><i><b></b></i><i><b></b></i><i><b></b></i></div>
  <div class="copy">© Copyright-2019 Follow the quiet river. All rights reserved.</div>
</footer>
</body>
</html>
```